Harvest Bridge Christian Ministry needs a Conference Ad

We are a Christian nonprofit focused on eliminating systemic poverty and helping believers function as ministers in their workplaces. The 2025 Lantern Path Global Conference coming up in October, and we need an ad for social media (facebook, instagram, and X) and our website in order to get people excited to attend! We are looking for a modern and sleek design that incorporates our logo (attached file). You can either put just the butterfly and then write our company name separately somewhere in the design or use it as is (we used Gotham font for the logo). We want to emphasize the joy of in-person connection at the conference, so you could possibly include stock photos of young people gathering together. You could also include the attached photo of our founders in the design and say “with Mel and Dora Quintavan". Also, include the conference dates, which are October 9-12, 2025, and say “come in person or join online”. Lastly, please include the tagline “from the Pellmore Awakening to Worldwide Transformation”. NOTE: I’m attaching AN EXAMPLE I’ve created of how the design could look, which you can feel free to use for inspiration.
Young people on Instagram and facebook
- Gotham

```html
<!DOCTYPE html>
<html lang="en">
<head>
<meta charset="utf-8">
<title>Lantern Path Global Conference 2025 – Harvest Bridge Christian Ministry</title>
<link rel="stylesheet" href="https://fonts.googleapis.com/css2?family=Montserrat:wght@300;400;500;600;800&family=Yellowtail&display=swap">
<style>
  :root {
    --stage: #a9a9a9;
    --navy: #0c1b4d;
    --royal: #2340a8;
    --bright-blue: #2f5be0;
    --purple: #6a3fb0;
    --violet: #4a3aa6;
    --gold: #f6d31a;
    --white: #ffffff;
    --grey-text: #5c5c66;
    --join-blue: #2a55d6;
    --photo-warm: #7a4a30;
    --photo-dark: #1b1512;
  }
  * { margin: 0; padding: 0; box-sizing: border-box; }
  html, body {
    width: 1200px; height: 796px; overflow: hidden;
    background: var(--stage);
  }
  .ad {
    position: absolute; left: 220px; top: 18px;
    width: 760px; height: 760px; display: block;
    box-shadow: 0 6px 18px rgba(0,0,0,.25);
  }
  .headline { font-family: "Montserrat", sans-serif; fill: var(--white); font-size: 67px; }
  .headline .light { font-weight: 300; }
  .headline .bold { font-weight: 800; letter-spacing: 1px; }
  .brand-name { font-family: "Montserrat", sans-serif; font-weight: 600; fill: var(--white); font-size: 24px; }
  .date-days { font-family: "Montserrat", sans-serif; font-weight: 500; fill: var(--gold); font-size: 66px; }
  .date-month { font-family: "Montserrat", sans-serif; font-weight: 300; fill: var(--white); font-size: 27px; }
  .date-year { font-family: "Montserrat", sans-serif; font-weight: 600; fill: var(--gold); font-size: 19px; letter-spacing: 8px; }
  .event-script { font-family: "Yellowtail", cursive; fill: var(--gold); }
  .event-year { font-family: "Montserrat", sans-serif; font-weight: 300; fill: var(--white); font-size: 50px; font-style: italic; }
  .cta-top { font-family: "Montserrat", sans-serif; font-weight: 500; fill: var(--grey-text); font-size: 33px; }
  .cta-or { font-family: "Montserrat", sans-serif; font-weight: 400; fill: var(--grey-text); font-size: 33px; }
  .cta-join { font-family: "Montserrat", sans-serif; font-weight: 600; fill: var(--join-blue); font-size: 33px; }
  .hosts { font-family: "Montserrat", sans-serif; font-weight: 400; font-size: 31px; fill: var(--white); }
  .hosts .names { fill: var(--gold); }
</style>
</head>
<body>
<svg class="ad" viewBox="0 0 1080 1080" xmlns="http://www.w3.org/2000/svg">
  <defs>
    <linearGradient id="bg-fade" x1="0" y1="0" x2="0" y2="1">
      <stop offset="0" stop-color="var(--bright-blue)"/>
      <stop offset=".45" stop-color="var(--royal)"/>
      <stop offset=".75" stop-color="#15296f"/>
      <stop offset="1" stop-color="var(--navy)"/>
    </linearGradient>
    <linearGradient id="badge-fill" x1="0" y1="0" x2="0" y2="1">
      <stop offset="0" stop-color="#2d3aa0"/>
      <stop offset="1" stop-color="var(--purple)"/>
    </linearGradient>
    <linearGradient id="band-fill" x1="0" y1="0" x2="1" y2="0">
      <stop offset="0" stop-color="var(--purple)"/>
      <stop offset="1" stop-color="var(--violet)"/>
    </linearGradient>
    <radialGradient id="portrait-fill" cx=".45" cy=".4" r=".7">
      <stop offset="0" stop-color="var(--photo-warm)"/>
      <stop offset="1" stop-color="var(--photo-dark)"/>
    </radialGradient>
    <clipPath id="ad-bounds"><rect width="1080" height="1080"/></clipPath>
  </defs>

  <g clip-path="url(#ad-bounds)">
    <!-- background crowd area -->
    <rect class="crowd-photo" width="1080" height="1080" fill="url(#bg-fade)" role="img" aria-label="Blue-tinted photo of young people gathering together joyfully"/>

    <!-- white corner -->
    <polygon class="corner-white" points="725,0 1080,0 1080,355" fill="var(--white)"/>

    <!-- brand -->
    <g class="brand">
      <circle cx="72" cy="106" r="14" fill="var(--white)"/>
      <text class="brand-name" x="98" y="115">HARVEST BRIDGE</text>
    </g>

    <!-- date badge -->
    <g class="date-badge">
      <circle cx="893" cy="168" r="113" fill="var(--white)"/>
      <circle cx="893" cy="168" r="102" fill="url(#badge-fill)"/>
      <text class="date-days" x="893" y="168" text-anchor="middle">9-12</text>
      <text class="date-month" x="893" y="197" text-anchor="middle">OCTOBER</text>
      <text class="date-year" x="897" y="222" text-anchor="middle">–2025–</text>
    </g>

    <!-- headline -->
    <text class="headline">
      <tspan class="light" x="46" y="302">FROM THE</tspan>
      <tspan class="bold" x="46" y="373">PELLMORE AWAKENING</tspan>
      <tspan x="46" y="445"><tspan class="light">TO </tspan><tspan class="bold">WORLDWIDE</tspan></tspan>
      <tspan class="bold" x="46" y="516">TRANSFORMATION</tspan>
    </text>

    <!-- event name -->
    <g class="event-title">
      <text class="event-script" x="388" y="660" text-anchor="end" font-size="78">Global</text>
      <text class="event-script" x="380" y="722" text-anchor="end" font-size="78">Conference</text>
      <polygon points="415,618 505,618 490,670 400,670" fill="var(--purple)"/>
      <polygon points="400,674 490,674 505,726 415,726" fill="var(--violet)"/>
      <text class="event-year" x="448" y="663" text-anchor="middle">20</text>
      <text class="event-year" x="448" y="719" text-anchor="middle">25</text>
    </g>

    <!-- call to action -->
    <g class="cta-pill">
      <rect x="88" y="770" width="372" height="102" rx="51" fill="var(--white)" stroke="var(--violet)" stroke-width="4"/>
      <text class="cta-top" x="274" y="813" text-anchor="middle">Come in-person</text>
      <text x="274" y="851" text-anchor="middle"><tspan class="cta-or">or </tspan><tspan class="cta-join">Join Online</tspan></text>
    </g>

    <!-- founders portrait -->
    <g class="portrait">
      <path d="M925,527 A345,345 0 0 0 580,872" fill="none" stroke="var(--white)" stroke-width="2"/>
      <path d="M568,1000 A360,360 0 0 1 560,870" fill="none" stroke="var(--white)" stroke-width="2"/>
      <path d="M1080,600 A360,360 0 0 0 910,540" fill="none" stroke="var(--white)" stroke-width="2"/>
      <path d="M590,770 A345,345 0 0 0 660,1080" fill="none" stroke="var(--white)" stroke-width="2"/>
      <circle cx="923" cy="527" r="6" fill="var(--white)"/>
      <circle cx="589" cy="770" r="6" fill="var(--white)"/>
      <circle cx="568" cy="976" r="6" fill="var(--white)"/>
      <circle cx="910" cy="875" r="320" fill="var(--white)"/>
      <circle cx="910" cy="875" r="310" fill="url(#portrait-fill)" role="img" aria-label="Photo of founders Mel and Dora Quintavan smiling together"/>
    </g>

    <!-- hosts band -->
    <g class="hosts-band">
      <path d="M0,960 H478 A30,30 0 0 1 478,1020 H0 Z" fill="url(#band-fill)"/>
      <text class="hosts" x="94" y="1001">with <tspan class="names">Mel &amp; Dora Quintavan</tspan></text>
    </g>
  </g>
</svg>
</body>
</html>
```